DENTIST OFFICE POST CARD DESIGN

COMPANY NAME: BEARABLE DENTISTRYCome and see if Meridale Dentistry is for you.... ALWAYSWELCOMINGNEW PATIENTS!Call today for your appointment!607 918 2763 We are located on 14 Palvin Street , Oneonta, Ny----(map scketch)All in one stop for all your dental care needsCOSMETIC DENTISTRYDENTAL IMPLANTSROOT CANALSVENEERSWHITENINGSFILLINGSCROWNSBRIDGESDENTURESEXTRACTIONSGUM TREATMENTSSNAP ON SMILECOLOR------ANYPOSTCARD INDICIA;PRSRT STDECRWSSU.S. POSTAGEPAIDEDDM RETAILLocalPostal Customer

```html
<!DOCTYPE html>
<html lang="en">
<head>
<meta charset="utf-8">
<title>Meridale Dentistry Postcard</title>
<link rel="stylesheet" href="https://fonts.googleapis.com/css2?family=Cinzel:wght@600;700&family=Libre+Baskerville:wght@400;700&family=Roboto+Condensed:wght@700&family=Dancing+Script:wght@700&display=swap">
<style>
  :root {
    --brand-blue: #1f5fa6;
    --deep-blue: #184f8f;
    --band-blue: #2166ae;
    --alert-red: #e0202a;
    --rule-grey: #c7c7c7;
    --page-bg: #2a2a2a;
    --card-white: #ffffff;
    --ink-dark: #333333;
  }
  * { margin: 0; padding: 0; box-sizing: border-box; }
  html, body { width: 1200px; height: 1173px; overflow: hidden; }
  body { background: var(--page-bg); position: relative; font-family: "Libre Baskerville", serif; }

  .card { position: absolute; background: var(--card-white); overflow: hidden; }
  .card-front { left: 115px; top: 20px; width: 928px; height: 508px; }
  .card-back { left: 117px; top: 593px; width: 926px; height: 503px; }

  .front-photo {
    position: absolute; left: 0; top: 0; width: 928px; height: 404px;
    background:
      radial-gradient(ellipse 260px 300px at 230px 230px, rgba(222,170,140,0.85) 0%, rgba(222,170,140,0) 100%),
      radial-gradient(ellipse 200px 260px at 60px 150px, rgba(70,45,35,0.75) 0%, rgba(70,45,35,0) 100%),
      radial-gradient(ellipse 180px 260px at 840px 210px, rgba(214,176,160,0.8) 0%, rgba(214,176,160,0) 100%),
      radial-gradient(ellipse 420px 90px at 420px 400px, rgba(240,215,190,0.9) 0%, rgba(240,215,190,0) 100%),
      linear-gradient(90deg, #f1f1f3 0%, #f6f7f9 50%, #e4e7ec 80%, #d6d9de 100%);
  }
  .front-headline {
    position: absolute; left: 96px; width: 800px; top: 24px; text-align: center;
    color: var(--brand-blue);
  }
  .front-headline .line { font-size: 20px; line-height: 25px; font-weight: 700; letter-spacing: 0.2px; }
  .front-headline .line-light { font-weight: 400; }
  .front-headline .cta { font-size: 19px; line-height: 27px; font-weight: 700; color: var(--deep-blue); }
  .front-headline .phone {
    font-family: "Roboto Condensed", sans-serif; font-size: 41px; line-height: 46px;
    color: var(--brand-blue); margin-top: 2px;
  }
  .front-band {
    position: absolute; left: 0; top: 404px; width: 928px; height: 104px; background: var(--band-blue);
  }
  .band-name {
    position: absolute; left: 26px; top: -2px; font-family: "Cinzel", serif; font-weight: 700;
    font-size: 64px; letter-spacing: 5px; color: #fff; white-space: nowrap;
  }
  .band-tagline {
    position: absolute; right: 42px; top: 60px; font-family: "Dancing Script", cursive;
    font-size: 28px; color: #fff; white-space: nowrap;
  }

  .back-name {
    position: absolute; left: 25px; top: 28px; font-family: "Cinzel", serif; font-weight: 700;
    font-size: 20px; letter-spacing: 2px; color: var(--brand-blue); white-space: nowrap;
  }
  .back-address {
    position: absolute; left: 52px; top: 51px; font-size: 11px; letter-spacing: 1px; color: var(--brand-blue);
  }
  .back-web {
    position: absolute; left: 25px; top: 65px; font-size: 13px; font-weight: 700; letter-spacing: 1.6px; color: var(--deep-blue);
  }
  .back-map {
    position: absolute; left: 25px; top: 95px; width: 261px; height: 212px;
    border: 3px solid var(--deep-blue);
    background:
      radial-gradient(ellipse 60px 40px at 230px 170px, #c9e3b4 0%, rgba(201,227,180,0) 100%),
      radial-gradient(ellipse 40px 30px at 100px 70px, #cfe3bf 0%, rgba(207,227,191,0) 100%),
      linear-gradient(135deg, #e6e5e0 0%, #dddcd6 100%);
  }
  .services-intro {
    position: absolute; left: 24px; top: 316px; font-size: 9.5px; line-height: 14px; font-weight: 700;
    color: var(--alert-red); letter-spacing: 0.2px;
  }
  .services-list {
    position: absolute; left: 24px; top: 352px; list-style: none;
    font-size: 10.5px; line-height: 13.9px; color: var(--brand-blue); letter-spacing: 0.3px;
  }
  .services-list li::before {
    content: ""; display: inline-block; width: 3px; height: 3px; background: var(--alert-red);
    margin-right: 8px; vertical-align: middle;
  }
  .postage-indicia {
    position: absolute; right: 30px; top: 28px; width: 112px; padding: 6px 4px;
    border: 1px solid var(--ink-dark); text-align: center;
    font-family: "Roboto Condensed", sans-serif; font-size: 10px; line-height: 13px;
    color: var(--ink-dark); letter-spacing: 0.4px;
  }
  .recipient-label {
    position: absolute; left: 592px; top: 318px; font-size: 10px; letter-spacing: 0.4px; color: var(--ink-dark);
  }
  .address-lines { position: absolute; left: 592px; top: 0; }
  .address-lines span {
    position: absolute; left: 0; width: 278px; height: 1px; background: var(--rule-grey);
  }
</style>
</head>
<body>
  <section class="card card-front">
    <div class="front-photo" role="img" aria-label="Photo of a smiling patient in a dental chair with a dentist holding a mouth mirror"></div>
    <div class="front-headline">
      <p class="line">COME AND SEE IF MERIDALE DENTISTRY</p>
      <p class="line">IS FOR YOU....</p>
      <p class="line">ALWAYS</p>
      <p class="line line-light">WELCOMING</p>
      <p class="line line-light">NEW PATIENTS!</p>
      <p class="cta">Call today for your appointment!</p>
      <p class="phone">607 918 2763</p>
    </div>
    <div class="front-band">
      <h1 class="band-name">MERIDALE&nbsp; DENTISTRY</h1>
      <p class="band-tagline">We'll Provide You With That Winning Smile!</p>
    </div>
  </section>

  <section class="card card-back">
    <h2 class="back-name">MERIDALE&nbsp; DENTISTRY</h2>
    <p class="back-address">14 PALVIN STREET, ONEONTA, NY</p>
    <p class="back-web">WWW.MERIDALEDENTIST.COM</p>
    <div class="back-map" role="img" aria-label="Street map showing the office location in Oneonta"></div>
    <p class="services-intro">OUR OFFICE PROVIDES ALL-IN-ONE STOP<br>SERVICES FOR ALL YOUR DENTAL CARE NEEDS</p>
    <ul class="services-list">
      <li>COSMETIC DENTISTRY</li>
      <li>DENTAL IMPLANTS</li>
      <li>ROOT CANALS</li>
      <li>VENEERS WHITENINGS</li>
      <li>FILLINGS CROWNS</li>
      <li>BRIDGES DENTURES</li>
      <li>EXTRACTIONS GUM</li>
      <li>TREATMENTS CLIP FIT GRIN COLOR</li>
    </ul>
    <div class="postage-indicia">
      <p>PRSRT STD</p>
      <p>ECRWSS</p>
      <p>U.S. POSTAGE</p>
      <p>PAID</p>
      <p>EDDM RETAIL</p>
    </div>
    <p class="recipient-label">Local Postal Customer</p>
    <div class="address-lines">
      <span style="top:344px"></span>
      <span style="top:402px"></span>
      <span style="top:459px"></span>
    </div>
  </section>
</body>
</html>
```